Flayer design for American style Pizza Company

We need to enhance an A5 flayer which we didn’t print yet because it doesn’t look good. We will send the file to the designer (PSD format) and we need a design that look like a fast food companies (QRB, Grill Meadow, Tolvins ,,etc.). Also some products picture which are included in the file needs to be improved (brightness , contrast, size, etc.). We may also provied the origenal master photos for the products.

please download the main files from http://dropvault.example/xKqTmwRzaP

Please dowload Products Pictures from http://dropvault.example/p4hWseLc7D

please download the main files from     http://dropvault.example/xKqTmwRzaP                     

hi all

Best Regards       

                                   

                                        Please dowload Products Pictures from     http://dropvault.example/p4hWseLc7D     

                                   

Reason: Hi all I guarantee to accept the design which sticks with the requirements. The submitted design will be compared before approval with ,Grill Meadow, QRB, Crust Barn etc designs. GoodLuck all Best Regards

```html
<!DOCTYPE html>
<html lang="ar" dir="rtl">
<head>
<meta charset="utf-8">
<title>أوفن لين — فطائر التورتيلا</title>
<link rel="stylesheet" href="https://fonts.googleapis.com/css2?family=Cairo:wght@700;900&family=Arimo:wght@700&family=Roboto+Condensed:wght@700&display=swap">
<style>
  :root{
    --green-dark:#5f7a35;
    --green:#7b9445;
    --green-light:#a9bf7a;
    --mint:#e4efdc;
    --cream:#f6f8f0;
    --red:#e5262b;
    --red-deep:#c41a1f;
    --ink:#1a1a1a;
    --band:#262626;
    --white:#ffffff;
  }
  *{margin:0;padding:0;box-sizing:border-box}
  html,body{width:853px;height:1200px;overflow:hidden;background:var(--white)}
  .flyer{position:relative;width:853px;height:1200px;overflow:hidden;
    background:linear-gradient(180deg,var(--cream) 0%,var(--mint) 45%,var(--green-light) 100%);}
  .header-band{position:absolute;inset:0 0 auto 0;height:300px;
    background:linear-gradient(180deg,var(--green-dark),var(--green));}
  .header-curve{position:absolute;left:0;top:180px;width:853px;height:140px}
  .brand{position:absolute;top:80px;right:45px;display:flex;align-items:center;gap:14px;direction:rtl}
  .brand-dot{width:26px;height:26px;border-radius:50%;background:var(--white)}
  .brand-name{font-family:"Cairo",sans-serif;font-weight:900;font-size:46px;color:var(--white);line-height:1.2}
  .halal-badge{position:absolute;top:52px;left:35px;width:115px;height:115px;border-radius:50%;
    border:4px solid var(--white);background:var(--ink)}
  .headline{position:absolute;top:290px;left:0;width:853px;text-align:center;
    font-family:"Cairo",sans-serif;font-weight:900;font-size:68px;color:var(--red);line-height:1.3;
    -webkit-text-stroke:3px var(--ink);paint-order:stroke fill;text-shadow:0 4px 6px rgba(0,0,0,.35)}
  .product-photo{position:absolute;top:413px;left:10px;width:820px;height:430px;border-radius:30px;
    background:radial-gradient(ellipse at 50% 55%,#e3b98a 0%,#d29a63 35%,rgba(200,120,80,.35) 65%,rgba(230,240,225,0) 80%)}
  .new-badge{position:absolute;top:493px;left:648px;width:150px;height:150px}
  .delivery{position:absolute;top:896px;left:0;width:853px;text-align:center;color:var(--red);
    font-size:34px;line-height:1.3;display:flex;justify-content:center;gap:12px;align-items:baseline}
  .delivery-ar{font-family:"Cairo",sans-serif;font-weight:700}
  .delivery-en{font-family:"Roboto Condensed",sans-serif;font-weight:700}
  .phone{position:absolute;top:964px;left:0;width:853px;text-align:center;
    font-family:"Arimo",sans-serif;font-weight:700;font-size:106px;color:var(--red);letter-spacing:2px;line-height:1;
    text-shadow:0 2px 0 var(--red-deep)}
  .tagline-band{position:absolute;bottom:0;left:0;width:853px;height:104px;background:var(--band);
    display:flex;align-items:center;justify-content:center}
  .tagline{font-family:"Cairo",sans-serif;font-weight:900;font-size:46px;line-height:1.2;color:var(--white);
    -webkit-text-stroke:2px var(--ink);paint-order:stroke fill}
</style>
</head>
<body>
<main class="flyer">
  <div class="header-band"></div>
  <svg class="header-curve" viewBox="0 0 853 140" preserveAspectRatio="none" aria-hidden="true">
    <path d="M0 100 Q426 -20 853 100 L853 140 L0 140 Z" fill="#ffffff"/>
    <path d="M0 112 Q426 -4 853 112 L853 140 L0 140 Z" fill="#f6f8f0"/>
  </svg>

  <div class="brand">
    <span class="brand-dot"></span>
    <span class="brand-name">أوفن لين</span>
  </div>
  <div class="halal-badge" role="img" aria-label="شارة حلال"></div>

  <h1 class="headline">ابدأ يومك بفطائر التورتيلا</h1>

  <div class="product-photo" role="img" aria-label="صورة فطائر تورتيلا محمصة محشوة مع طماطم وفلافل وزيتون وأعشاب"></div>

  <svg class="new-badge" viewBox="0 0 150 150" aria-label="جديد">
    <polygon fill="#5f9a2e" stroke="#ffffff" stroke-width="4"
      points="75,4 88,22 108,12 112,35 135,35 128,57 146,70 128,85 138,106 114,110 110,134 89,124 75,146 61,124 40,134 36,110 12,106 22,85 4,70 22,57 15,35 38,35 42,12 62,22"/>
    <text x="75" y="92" text-anchor="middle" font-family="Cairo, sans-serif" font-weight="900" font-size="44" fill="#ffffff">جديد</text>
  </svg>

  <p class="delivery"><span class="delivery-ar">خدمة توصيل سريعة</span><span class="delivery-en" dir="ltr">Fast Delivery Service</span></p>
  <p class="phone" dir="ltr">048 662 190</p>

  <footer class="tagline-band">
    <p class="tagline">تورتيلا محمصة تصلك ساخنة وهشة</p>
  </footer>
</main>
</body>
</html>
```